Award winning pet photographer needs business card and letterhead

Business card and letterhead for our Pet photography business. We specialize in studio portraits of dogs.

Target Market(s)

Wealthy and middle class dog owners who would like photos of their dogs as wall art.

Industry/Entity Type

Portrait Photography

Contact Information for Business Card

Our business name is Tails of Glee Pet Photography. Would be good to include dog and a heart, bright colours and a modern design

Font styles to use
Sans Serif

Colors
f04a50
f68d4d
faa54b
33a6d7
33b8a4
abd036

Requirements
Must have
• Business name: Tails of Glee Pet Photography
• Phone number: 0497 560314
• Email: marcus@kwstudio.com.au
• Website:www.tailsofglee.com.au
• Photographer: Marcus Holloway
Nice to have
• In Addition letterhead should include
• Studio address 27 Fennick Court, Leederville 6007
• Postal Address 8 Ormsby Ave, West Leederville 6007

```html
<!DOCTYPE html>
<html lang="en">
<head>
<meta charset="utf-8">
<title>Tails of Glee Pet Photography – Business Card</title>
<link rel="stylesheet" href="https://fonts.googleapis.com/css2?family=Questrial&display=swap">
<style>
  :root {
    --backdrop: #8f8f8f;
    --card-dark: #2b2d2f;
    --card-dark-deep: #1e1f21;
    --card-light: #ffffff;
    --teal: #3fbfa9;
    --ink-light: #f2f2f2;
    --ink-dark: #2a2a2a;
  }
  * { box-sizing: border-box; margin: 0; padding: 0; }
  html, body { width: 1200px; height: 900px; overflow: hidden; }
  body {
    background: linear-gradient(180deg, #a9a9a9 0%, var(--backdrop) 60%, #777 100%);
    font-family: "Questrial", sans-serif;
    position: relative;
  }
  .card {
    position: absolute;
    top: 295px;
    width: 540px;
    height: 310px;
    border-radius: 22px;
    overflow: hidden;
    box-shadow: 0 18px 30px rgba(0,0,0,0.35);
  }
  .card--back { left: 40px; }
  .card--front { left: 620px; background: var(--card-light); }

  .card__texture {
    position: absolute; inset: 0;
    background: radial-gradient(ellipse at 60% 40%, var(--card-dark) 0%, var(--card-dark-deep) 100%);
  }

  .brand {
    position: absolute;
    display: flex;
    align-items: center;
    gap: 14px;
  }
  .brand__dot {
    width: 30px; height: 30px;
    border-radius: 50%;
    background: var(--teal);
    flex: none;
  }
  .brand__name {
    color: var(--teal);
    font-size: 27px;
    line-height: 1.15;
    letter-spacing: 0.5px;
    text-transform: uppercase;
  }
  .card--back .brand { left: 70px; top: 112px; }
  .card--front .brand { left: 40px; top: 50px; }

  .front__band {
    position: absolute; left: 0; top: 0;
    width: 540px; height: 310px;
  }
  .contact {
    position: absolute;
    left: 38px; top: 190px;
    color: var(--ink-light);
  }
  .contact__name { color: var(--teal); font-size: 20px; }
  .contact__role { font-size: 11px; margin-top: 3px; }
  .contact__list { list-style: none; margin-top: 20px; }
  .contact__item {
    display: flex; align-items: center; gap: 8px;
    font-size: 15px; line-height: 21px;
  }
  .contact__icon { width: 16px; height: 16px; flex: none; }
</style>
</head>
<body>

  <section class="card card--back">
    <div class="card__texture" role="img" aria-label="Dark perforated texture background"></div>
    <div class="brand">
      <span class="brand__dot"></span>
      <span class="brand__name">Tails of Glee<br>Pet Photography</span>
    </div>
  </section>

  <section class="card card--front">
    <svg class="front__band" viewBox="0 0 540 310" aria-hidden="true">
      <defs>
        <linearGradient id="darkFill" x1="0" y1="0" x2="0" y2="1">
          <stop offset="0" stop-color="#2f3133"/>
          <stop offset="1" stop-color="#1f2022"/>
        </linearGradient>
      </defs>
      <polygon points="0,172 540,152 540,310 0,310" fill="url(#darkFill)"/>
      <polygon points="0,166 540,146 540,153 0,173" fill="var(--teal)"/>
    </svg>

    <div class="brand">
      <span class="brand__dot"></span>
      <span class="brand__name">Tails of Glee<br>Pet Photography</span>
    </div>

    <div class="contact">
      <p class="contact__name">Marcus Holloway</p>
      <p class="contact__role">Photographer</p>
      <ul class="contact__list">
        <li class="contact__item">
          <svg class="contact__icon" viewBox="0 0 16 16" aria-hidden="true">
            <circle cx="8" cy="8" r="7" fill="none" stroke="var(--teal)" stroke-width="1.4"/>
            <path d="M5.5 4.5l1.5 1.5-1 1a5 5 0 0 0 3 3l1-1 1.5 1.5-1 1c-3 0-6-3-6-6z" fill="var(--teal)"/>
          </svg>
          0497 560314
        </li>
        <li class="contact__item">
          <svg class="contact__icon" viewBox="0 0 16 16" aria-hidden="true">
            <circle cx="8" cy="8" r="7" fill="none" stroke="var(--teal)" stroke-width="1.4"/>
            <rect x="4.5" y="5.5" width="7" height="5" fill="var(--teal)"/>
            <path d="M4.5 5.5l3.5 3 3.5-3" fill="none" stroke="var(--card-dark)" stroke-width="0.8"/>
          </svg>
          marcus@kwstudio.com.au
        </li>
        <li class="contact__item">
          <svg class="contact__icon" viewBox="0 0 16 16" aria-hidden="true">
            <circle cx="8" cy="8" r="7" fill="none" stroke="var(--teal)" stroke-width="1.4"/>
            <circle cx="8" cy="8" r="4" fill="none" stroke="var(--teal)" stroke-width="1"/>
            <path d="M4 8h8M8 4c-2 2-2 6 0 8M8 4c2 2 2 6 0 8" fill="none" stroke="var(--teal)" stroke-width="0.8"/>
          </svg>
          www.tailsofglee.com.au
        </li>
      </ul>
    </div>
  </section>

</body>
</html>
```